Nimbus Pay Hub Brochure

We offer payment processing and customer service solutions for the parents of Charter schools in the United States.
(More info: http://en.lorevaultex.org/page/Independent_academies_overview )

We have some content and are looking to make an 11x17 back and front design collateral piece. We are also looking for business cards and a 10'x10' trade show booth - separate projects but we can probably use the same designer across both.

Target Market(s)

School Administrators, people who work in school offices, specifically people who work with quickbooks or accounting software for schools.

Industry/Entity Type

Trade

Colors

Designer to choose colors to be used in the design.

Requirements
Must have
• Must have 2-4 pages, maybe 8 pages 1/2 size. It must use most of the content I included.
Nice to have
• I would like photos included - but realize that may not be possible given the space requirement.
Should not have
• Too many fonts, anything that is too glitzy.

```html
<!DOCTYPE html>
<html lang="en">
<head>
<meta charset="utf-8">
<title>Nimbus Pay Hub Brochure</title>
<link href="https://fonts.googleapis.com/css2?family=Open+Sans:wght@300;400;600;700&display=swap" rel="stylesheet">
<style>
:root{
  --blue:#1f5fa8;
  --sky:#2b8ccb;
  --navy:#1c56a0;
  --gray-1:#7a7a7a;
  --gray-2:#5e5e5e;
  --paper:#eeeef1;
  --ink:#222222;
  --muted:#8a8a8a;
  --white:#ffffff;
  --map:#dcdce0;
}
*{box-sizing:border-box;margin:0;padding:0}
html,body{width:926px;height:1200px;overflow:hidden;background:var(--white)}
body{font-family:"Open Sans",Arial,sans-serif;color:var(--ink);position:relative}
.abs{position:absolute}
.cover{left:0;top:0;width:926px;height:463px;background:linear-gradient(#f3f3f5 0%,#ececef 80%,#f6f6f8 100%)}
.section-title{font-weight:700;color:var(--blue);font-size:15px;letter-spacing:.2px;white-space:nowrap}
.band{position:absolute;left:0;width:926px;height:40px;display:flex;align-items:center;color:var(--white)}
.band--g1{background:linear-gradient(90deg,#6c6c6c,#8c8c8c)}
.band--g2{background:linear-gradient(90deg,#565656,#707070)}
.band--b1{background:var(--sky)}
.band--b2{background:var(--navy)}
.intro-line{font-weight:300;font-size:15px;padding-left:28px;white-space:nowrap}
.tag{position:absolute;left:490px;font-weight:300;font-size:16px;letter-spacing:.3px;white-space:nowrap}
.tag b{font-weight:700}
.photo{position:absolute}
.map{position:absolute;background:var(--map);opacity:.7}
.gift{left:148px;top:293px;width:168px;height:94px;border-radius:8px;background:#f8f8f8;border:1px solid #d4d4d4;padding:6px}
.gift-inner{width:100%;height:100%;border-radius:5px;background:linear-gradient(#2e2e2e,#121212);color:#fff;padding:6px 10px;font-size:9px;line-height:1.15}
.gift-brand{font-weight:700;font-size:10px}
.gift-amount{font-size:22px;font-weight:300;margin:4px 0 0 56px;line-height:1}
.gift-amount sup{font-size:10px}
.gift-note{margin-left:57px;font-size:9px;color:#ddd}
.brand{display:flex;align-items:center;gap:8px;color:var(--blue);font-weight:700;white-space:nowrap}
.brand-mark{display:block;background:var(--sky)}
.contact{font-size:11px;color:var(--muted);line-height:16px;white-space:nowrap}
.contact b{color:#111}
.badge{background:#cfd3d8}
.sub-note{font-size:6.5px;color:#222;letter-spacing:.2px;white-space:nowrap}
.pay-item{position:absolute;font-size:11px;color:var(--white);white-space:nowrap}
.pay-item::before{content:"\2713";margin-right:7px}
.types{left:493px;top:886px;list-style:none;font-size:8.6px;line-height:13.85px;color:#222;white-space:nowrap}
.types li::before{content:"\2713";margin-right:7px}
.cloud{left:300px;top:990px;width:120px;height:72px;border-radius:36px;background:var(--navy);border:3px solid #fff;color:#fff;font-size:14px;text-align:center;padding-top:14px;line-height:18px}
</style>
</head>
<body>

<!-- Cover panel -->
<div class="abs cover"></div>
<div class="map" role="img" aria-label="Faint grey map of the United States" style="left:365px;top:245px;width:270px;height:170px;border-radius:30px 60px 50px 20px"></div>
<h2 class="abs section-title" style="left:28px;top:52px">WHY NIMBUS PAY HUB</h2>

<div class="band band--g1" style="top:80px"><span class="intro-line">For over 25 years and with 2500 school</span><span class="tag">ANY CHILD</span></div>
<div class="band band--g2" style="top:120px"><span class="intro-line">customers, Nimbus has continued to earn</span><span class="tag">ANY GRADE</span></div>
<div class="band band--b1" style="top:160px"><span class="intro-line">stellar grades from both parents and</span><span class="tag">ANY PAYMENT</span></div>
<div class="band band--b2" style="top:199px"><span class="intro-line">school administrators.</span><span class="tag">EASILY <b>PAID</b></span></div>
<div class="abs" style="left:463px;top:80px;width:1px;height:159px;background:rgba(255,255,255,.35)"></div>

<svg class="abs" style="left:610px;top:80px" width="60" height="159" aria-hidden="true">
  <circle cx="18" cy="20" r="7" fill="#e8e8e8"/><circle cx="38" cy="20" r="7" fill="#8a8a8a"/>
  <circle cx="18" cy="60" r="7" fill="#e8e8e8"/><circle cx="38" cy="60" r="7" fill="#4a4a4a"/>
  <circle cx="18" cy="99" r="7" fill="#e8e8e8"/><circle cx="38" cy="99" r="7" fill="#1f78bd"/>
  <circle cx="18" cy="139" r="7" fill="none" stroke="#e8e8e8" stroke-width="2"/>
</svg>

<div class="photo" role="img" aria-label="Photo of a smiling school administrator in a cream cardigan gesturing toward the reader" style="left:660px;top:36px;width:266px;height:424px;background:linear-gradient(180deg,#c8b8a6 0%,#e9e2d8 55%,#f1ece5 100%);border-radius:110px 0 0 0"></div>

<div class="abs gift">
  <div class="gift-inner">
    <div class="gift-brand">arcmart</div>
    <div class="gift-amount"><sup>$</sup>100</div>
    <div class="gift-note">gift card for every<br>DEMO</div>
  </div>
</div>

<!-- Contact strip -->
<div class="abs brand" style="left:28px;top:512px;font-size:13px">
  <span class="brand-mark" style="width:24px;height:24px"></span>Nimbus Pay Hub
</div>
<div class="abs contact" style="left:28px;top:547px">
  Call&nbsp;&nbsp;&nbsp;: <b>1-800-555-0142</b><br>Email: <b>Sales@nimbuspayhub.com</b>
</div>
<div class="abs" style="left:323px;top:517px;width:1px;height:50px;background:#333"></div>
<div class="abs badge" style="left:333px;top:516px;width:104px;height:16px"></div>
<div class="abs badge" style="left:333px;top:538px;width:104px;height:22px"></div>
<div class="abs sub-note" style="left:333px;top:566px">A SUBSIDIARY OF BRIGHTLEDGER TUITION</div>

<div class="abs brand" style="left:706px;top:510px;font-size:20px">
  <span class="brand-mark" style="width:36px;height:36px"></span>Nimbus Pay Hub
</div>

<!-- How can they pay -->
<h2 class="abs section-title" style="left:28px;top:654px;font-weight:400;font-size:14px">HOW CAN THE PAY</h2>
<div class="band band--g1" style="top:680px"></div>
<div class="band band--g2" style="top:720px"></div>
<div class="band band--b1" style="top:759px"></div>
<div class="band band--b2" style="top:798px"></div>
<div class="photo" role="img" aria-label="Photo of a man in a blue checked shirt reviewing a clipboard at a laptop" style="left:560px;top:600px;width:366px;height:238px;background:linear-gradient(180deg,#cfd6de 0%,#9fb6cf 45%,#6f93bd 100%);border-radius:90px 0 0 0"></div>
<svg class="abs" style="left:505px;top:680px" width="60" height="158" aria-hidden="true">
  <circle cx="18" cy="20" r="7" fill="#f0f0f0"/><circle cx="38" cy="20" r="7" fill="#8a8a8a"/>
  <circle cx="18" cy="60" r="7" fill="#f0f0f0"/><circle cx="38" cy="60" r="7" fill="#4a4a4a"/>
  <circle cx="18" cy="99" r="7" fill="#f0f0f0"/><circle cx="38" cy="99" r="7" fill="#1f78bd"/>
  <circle cx="18" cy="139" r="7" fill="none" stroke="#f0f0f0" stroke-width="2"/>
</svg>

<span class="pay-item" style="left:28px;top:695px">Invoices</span>
<span class="pay-item" style="left:28px;top:733px">Mobile Payments</span>
<span class="pay-item" style="left:28px;top:771px">E-Invoices</span>
<span class="pay-item" style="left:28px;top:809px">Automatic Bank Transfers</span>
<span class="pay-item" style="left:184px;top:696px">Shopping Card</span>
<span class="pay-item" style="left:184px;top:734px">Credit Card Payments</span>
<span class="pay-item" style="left:184px;top:772px">Donation Handling</span>
<span class="pay-item" style="left:184px;top:810px">Phone Payments</span>
<span class="pay-item" style="left:323px;top:697px">In-Person Payments</span>
<span class="pay-item" style="left:323px;top:735px">Mailed Payments</span>

<div class="photo" role="img" aria-label="Photo of hands using a phone payment app on a wooden desk beside a white keyboard, coffee cup and newspaper" style="left:0;top:838px;width:463px;height:312px;background:linear-gradient(160deg,#d9d7d3 0%,#b9aa98 35%,#6e4f39 75%,#5a3f2c 100%)"></div>
<div class="abs cloud">Online<br>Payments</div>

<!-- Payment types -->
<div class="map" role="img" aria-label="Faint grey map of the United States" style="left:738px;top:852px;width:166px;height:92px;border-radius:18px 30px 36px 16px"></div>
<h2 class="abs" style="left:490px;top:858px;font-size:14px;font-weight:400;color:var(--blue);white-space:nowrap">WHAT TYPES OF PAYMENTS:</h2>
<ul class="abs types">
  <li>Payments for Damages/Repairs</li>
  <li>Payments for Goods/Services</li>
  <li>Payments for Extracurricular/Non-Curricular Activities</li>
  <li>Payments for Activities that Supplement a Class/Educational Program</li>
  <li>Payments for Uniforms/ Personal Athletic Equipment</li>
  <li>Payments for Registration / Security Deposits</li>
  <li>Payments for Extended Care Hours / Late Pickups</li>
  <li>Payments for Supplemental Field Trips</li>
  <li>Payments for Voluntary Student Insurance</li>
  <li>Payments for Technology Equipment / Musical Instruments</li>
  <li>Payments for Lab and Shop Classes</li>
  <li>Payments for Student Publications</li>
  <li>Payments for Graduation Announcements</li>
  <li>Payments for Class Rings</li>
  <li>Payments for Post-Secondary Instructional Programs</li>
  <li>Payments for Lost and Destroyed Textbooks/Workbooks/Library Books</li>
  <li>Payments for Voluntary Student Insurance</li>
  <li>Payments for Donations / Gifts</li>
</ul>

<div class="abs" style="left:463px;top:1140px;width:463px;height:60px;background:linear-gradient(#ffffff,#ececef)"></div>
<div class="abs brand" style="left:780px;top:1154px;font-size:12px">
  <span class="brand-mark" style="width:26px;height:26px"></span>Nimbus Pay Hub
</div>
<div class="abs" style="left:463px;top:0;width:1px;height:1200px;background:rgba(0,0,0,.04)"></div>
</body>
</html>
```